依頼詳細
サイト構成・基本的な要件については
https://zumora.example/diagrams/P3TR8xmaqelu2sHb
を併せてご覧いただければ幸いです。
※導線が確保されていれば、必ずしもレイアウト案に忠実である必要はございません。
ぜひご提案いただければ幸甚です。

また、素材については
http://nibulo-share.example/download/58174a2c9d3e0b6f1a7c4e2d9b8f0a6c3e5d7b1f
よりダウンロードいただければと存じます。

上記だけで制作が難しい場合は
http://moruka.example/
などから、5000円程度までならこちらにて購入可能です。カンプデータにて作成頂き、
納品時に当方にて購入したデータに差し替えていただければと存じます。

全体的なデザインのイメージとしては

http://www.tovira-hatake.example/
http://www.samolet.example/rollmode/
http://vesmira.example/
http://ri-kogetsu.example/
のような、白ベースですっきりと見やすい印象が希望です。

メインカラーは既存サイトと同様、グリーンでお願いします。
http://www.tobakitchen.example/
サイトURL
ページ数
1ページ
希望イメージ
シンプル 複雑
単色 カラフル
暗い 明るい
日常 高級
遊び心 厳粛
未来的 伝統的
女性的 男性的
希望する色
白を基調とし、グリーンベースでスッキリと明るく見やすいデザインを希望します
納品ファイル
• 高解像度JPG (.jpg)
• フォトショップ形式 (.psd)
補足説明
素材については
よりダウンロードいただければと存じます。

上記だけで制作が難しい場合は
http://moruka.example/

白ベースでメインカラーは既存と同様にグリーンを使用し、
明るく見やすいデザインをお願いできればと思います。

http://bottom-parts.example/2012/166.html
http://bottom-parts.example/2011/115.html
→フッター部分の参照

基本レイアウト
については、必ずしも忠実である必要はありません。

是非ご提案お待ちしております。
何卒よろしくお願いいたします。

制作につきましてご不明な点がございましたら、お気軽にお申し付けいただければと存じます。
ご提案お待ちしております。

クライアント様との協議の結果こちらの案を採用させていただきました。
高級感と柔らかさのバランスがとてもよく、
視認性も高く、要望を全て満たしておりましたので
こちらの案を採用いたしました。

この度は多数ご提案いただきありがとうございました。
当選に至らなかったランサー様におかれましては大変心苦しいのですが、
またの機会にぜひご提案いただければ幸甚です。
引き続き何卒よろしくお願いいたします。

```html
<!DOCTYPE html>
<html lang="ja">
<head>
<meta charset="utf-8">
<title>鳥羽キッチン</title>
<link rel="stylesheet" href="https://fonts.googleapis.com/css2?family=Noto+Sans+JP:wght@400;500;700&display=swap">
<style>
:root{
  --green:#3f9b2c;
  --green-dark:#2f7d1f;
  --green-light:#8cc63f;
  --green-pale:#eef6e4;
  --line:#cfe2bd;
  --text:#444;
  --muted:#777;
  --white:#fff;
  --bg:#f4f4f0;
}
*{box-sizing:border-box;margin:0;padding:0}
html,body{width:841px;height:1200px;overflow:hidden}
body{font-family:"Noto Sans JP",sans-serif;color:var(--text);background:var(--white);font-size:9px;line-height:1.5;position:relative}
.site-header{position:absolute;left:0;top:0;width:841px;height:44px;border-bottom:1px solid var(--line)}
.brand{position:absolute;left:40px;top:6px;display:flex;align-items:center;gap:8px}
.brand-mark{width:30px;height:30px;border-radius:50%;background:var(--green)}
.brand-sub{display:block;font-size:8px;color:var(--green);line-height:1}
.brand-name{display:block;font-size:19px;font-weight:700;color:var(--green);line-height:1.2}
.util{position:absolute;left:560px;top:8px;display:flex;gap:3px}
.util a{display:block;width:42px;height:16px;border:1px solid var(--line);text-align:center;font-size:8px;line-height:14px;color:var(--green-dark);text-decoration:none;background:var(--white)}
.cta-box{position:absolute;left:700px;top:5px;width:118px;height:32px;background:var(--green);color:var(--white);font-size:8px;line-height:1.35;padding:5px 8px;font-weight:500}
.hero{position:absolute;left:0;top:44px;width:841px;height:225px;background:linear-gradient(#fafaf6,#f1efe8)}
.tagline{text-align:center;font-size:10px;color:var(--green-dark);padding-top:10px;font-weight:500}
.spices{position:absolute;left:70px;top:30px;width:700px;height:185px;border-radius:4px;background:linear-gradient(90deg,#d7a048,#b7a56d 20%,#8f8b55 40%,#c9964f 60%,#9f3b2a 80%,#7d8a3a)}
.global-nav{position:absolute;left:70px;top:283px;width:700px;display:flex;gap:4px}
.global-nav a{flex:1;height:30px;border:1px solid var(--green-light);border-radius:3px;text-align:center;line-height:28px;font-size:9px;color:var(--green-dark);text-decoration:none;font-weight:500}
.sidebar{position:absolute;left:70px;top:338px;width:165px}
.trial{border:2px solid var(--green);background:var(--white);padding:6px 8px;height:150px}
.trial h2{font-size:15px;color:var(--green);line-height:1.3;text-align:center}
.trial .note{font-size:8px;text-align:center;color:var(--muted);margin:2px 0 6px}
.tel{display:flex;align-items:center;gap:5px;font-size:13px;font-weight:700;color:var(--green-dark);margin-top:4px}
.tel svg{width:14px;height:14px}
.trial .hours{font-size:8px;color:var(--muted);margin-top:5px;text-align:center}
.side-menu{margin-top:12px;border:1px solid var(--line)}
.side-menu h3{background:var(--green);color:var(--white);font-size:10px;padding:3px 8px}
.side-menu ul{list-style:none}
.side-menu li{border-bottom:1px dotted var(--line);padding:4px 8px 4px 16px;font-size:8.5px;position:relative}
.side-menu li::before{content:"";position:absolute;left:7px;top:9px;border-left:4px solid var(--green);border-top:3px solid transparent;border-bottom:3px solid transparent}
.friend-banner{margin-top:10px;height:48px;background:var(--green);color:var(--white);font-size:12px;font-weight:700;text-align:center;line-height:48px;border-radius:3px}
.main{position:absolute;left:246px;top:338px;width:524px}
.info-row{display:flex;gap:12px;height:120px}
.info-box{flex:1;border:1px solid var(--line)}
.info-box h3{background:var(--green);color:var(--white);font-size:10px;padding:3px 8px;display:flex;justify-content:space-between}
.info-box h3 small{font-size:7px;font-weight:400}
.info-box ul{list-style:none;padding:4px 8px}
.info-box li{font-size:8px;border-bottom:1px dotted var(--line);padding:3px 0;display:flex;gap:8px}
.info-box time{color:var(--green-dark)}
.section-title{margin-top:12px;background:var(--green);color:var(--white);font-size:11px;padding:4px 10px;font-weight:500}
.cards{display:grid;grid-template-columns:1fr 1fr;gap:10px 10px;margin-top:10px}
.card{height:104px;border:1px solid var(--line);position:relative}
.card-photo{height:64px;background:linear-gradient(135deg,#e9dcc7,#c9b79a)}
.card-photo.p2{background:linear-gradient(135deg,#efe6d8,#b99e7d)}
.card-photo.p3{background:linear-gradient(135deg,#f3efe6,#a9b79b)}
.card-photo.p4{background:linear-gradient(135deg,#e2d3bd,#a48466)}
.card-photo.p5{background:linear-gradient(135deg,#f0e8dc,#c8a47e)}
.card-photo.p6{background:linear-gradient(135deg,#e5e0d0,#b4915f)}
.card h4{position:absolute;left:0;top:6px;background:rgba(63,155,44,.9);color:var(--white);font-size:10px;padding:2px 10px}
.card p{font-size:7.5px;padding:4px 8px;line-height:1.45;color:var(--muted)}
.course-links{position:absolute;left:70px;top:898px;width:700px;display:flex;gap:10px}
.course-links a{flex:1;height:28px;border:1px solid var(--green-light);border-radius:14px;text-align:center;line-height:26px;font-size:9px;color:var(--green-dark);text-decoration:none;font-weight:500}
.site-footer{position:absolute;left:0;top:945px;width:841px;height:255px;background:var(--green-pale);border-top:3px solid var(--green)}
.schools{position:absolute;left:70px;top:10px;width:700px;display:flex;gap:16px}
.school{flex:1;font-size:7.5px;line-height:1.6}
.school strong{color:var(--green-dark);font-size:8.5px;display:block}
.foot-nav{position:absolute;left:70px;top:72px;width:700px;border-top:1px solid var(--line);border-bottom:1px solid var(--line);display:flex;justify-content:space-between;padding:4px 6px;font-size:7.5px;color:var(--green-dark)}
.foot-cta{position:absolute;left:70px;top:98px;width:700px;height:54px;background:var(--green);display:flex;align-items:center;padding:0 14px;gap:14px;color:var(--white)}
.foot-cta .lead{font-size:12px;font-weight:700;flex:1}
.foot-cta .mail{background:var(--white);color:var(--green-dark);font-size:9px;padding:6px 14px;border-radius:3px;font-weight:500}
.foot-cta .foot-brand{display:flex;align-items:center;gap:6px;font-size:14px;font-weight:700}
.foot-cta .foot-brand i{width:18px;height:18px;border-radius:50%;background:var(--white);display:block}
.copyright{position:absolute;left:0;top:170px;width:841px;text-align:center;font-size:7.5px;color:var(--muted)}
</style>
</head>
<body>
<header class="site-header">
  <div class="brand">
    <span class="brand-mark"></span>
    <span><span class="brand-sub">toba kitchen school</span><span class="brand-name">鳥羽キッチン</span></span>
  </div>
  <nav class="util"><a href="#">資料請求</a><a href="#">体験申込</a><a href="#">アクセス</a></nav>
  <div class="cta-box">無料レッスン・資料請求<br>お問い合わせはこちら</div>
</header>

<section class="hero">
  <p class="tagline">一人ひとりの笑顔にこだわり、家庭料理から本格料理まで「お・も・て・な・し」料理を丁寧にお教えします。</p>
  <div class="spices" role="img" aria-label="スプーンに盛られた色とりどりのスパイスの写真"></div>
</section>

<nav class="global-nav">
  <a href="#">ホーム</a><a href="#">鳥羽キッチンについて</a><a href="#">入会案内</a><a href="#">コース案内</a><a href="#">教室案内</a><a href="#">料金表</a><a href="#">よくあるご質問</a>
</nav>

<aside class="sidebar">
  <div class="trial">
    <h2>見学・体験レッスン<br>受付中！</h2>
    <p class="note">見学・体験はお気軽にどうぞ</p>
    <div class="tel"><svg viewBox="0 0 14 14"><path d="M3 1l2 3-1.5 1.5c.8 1.8 2.2 3.2 4 4L9 8l3 2-1 3C6 13 1 8 1 3z" fill="#3f9b2c"/></svg>03-5550-0182</div>
    <div class="tel"><svg viewBox="0 0 14 14"><path d="M3 1l2 3-1.5 1.5c.8 1.8 2.2 3.2 4 4L9 8l3 2-1 3C6 13 1 8 1 3z" fill="#3f9b2c"/></svg>0120-555-0318</div>
    <p class="hours">受付時間 10:00〜18:00</p>
  </div>
  <div class="side-menu">
    <h3>メニュー</h3>
    <ul>
      <li>ホーム</li><li>鳥羽キッチンについて</li><li>入会案内</li><li>コース案内</li><li>教室案内</li><li>料金表</li><li>よくあるご質問</li><li>お問い合わせ</li>
    </ul>
  </div>
  <div class="friend-banner">お友達の皆様へ</div>
</aside>

<main class="main">
  <div class="info-row">
    <section class="info-box">
      <h3>新着情報<small>一覧へ</small></h3>
      <ul>
        <li><time>2014.03.20</time>春の体験レッスンを開始しました</li>
        <li><time>2014.03.10</time>今月のメニューを更新しました</li>
        <li><time>2014.03.01</time>短期集中コースの受付開始</li>
        <li><time>2014.02.20</time>サンデーコースの日程変更</li>
        <li><time>2014.02.10</time>教室のご案内を更新しました</li>
      </ul>
    </section>
    <section class="info-box">
      <h3>今月のメニュー<small>一覧へ</small></h3>
      <ul>
        <li><time>R101</time>春野菜のちらし寿司</li>
        <li><time>R102</time>鯛の酒蒸し 木の芽添え</li>
        <li><time>R103</time>若竹煮とお吸い物</li>
        <li><time>R104</time>季節のデザート</li>
      </ul>
    </section>
  </div>

  <h2 class="section-title">鳥羽キッチンについて</h2>
  <div class="cards">
    <article class="card"><div class="card-photo" role="img" aria-label="料理教室で調理する様子の写真"></div><h4>鳥羽キッチンの特徴</h4><p>一人ひとりに寄り添った丁寧な指導で、<br>毎日の料理がもっと楽しくなります。</p></article>
    <article class="card"><div class="card-photo p2" role="img" aria-label="食材を切る手元の写真"></div><h4>レギュラーコース</h4><p>基本から学べる定番のコースです。<br>家庭料理の腕を着実に磨けます。</p></article>
    <article class="card"><div class="card-photo p3" role="img" aria-label="盛り付けられた料理の写真"></div><h4>専門・特別コース</h4><p>和食・洋食・製菓など専門的な<br>技術をじっくり学べます。</p></article>
    <article class="card"><div class="card-photo p4" role="img" aria-label="鍋で煮込む料理の写真"></div><h4>短期集中コース</h4><p>短い期間で基礎をしっかり<br>身につけたい方におすすめです。</p></article>
    <article class="card"><div class="card-photo p5" role="img" aria-label="焼き菓子とデザートの写真"></div><h4>サンデーコース</h4><p>お仕事で平日お忙しい方も<br>日曜日に楽しく通えます。</p></article>
    <article class="card"><div class="card-photo p6" role="img" aria-label="季節の食材の写真"></div><h4>特別コース</h4><p>季節の行事やおもてなしに<br>ぴったりの料理を学べます。</p></article>
  </div>
</main>

<nav class="course-links">
  <a href="#">レギュラーコース</a><a href="#">専門・特別コース</a><a href="#">短期集中コース</a><a href="#">サンデーコース</a><a href="#">特別コース</a>
</nav>

<footer class="site-footer">
  <div class="schools">
    <div class="school"><strong>鳥羽キッチン 本校</strong>〒100-0000 東京都中央区港町1-2-3<br>TEL 03-5550-0182</div>
    <div class="school"><strong>鳥羽キッチン 西校</strong>〒100-0001 東京都新宿区緑町4-5-6<br>TEL 03-5550-0247</div>
    <div class="school"><strong>鳥羽キッチン 南校</strong>〒200-0002 神奈川県横浜市花町7-8-9<br>TEL 045-555-0391</div>
  </div>
  <nav class="foot-nav"><span>ホーム</span><span>鳥羽キッチンについて</span><span>入会案内</span><span>コース案内</span><span>教室案内</span><span>料金表</span><span>よくあるご質問</span><span>お問い合わせ</span><span>サイトマップ</span></nav>
  <div class="foot-cta">
    <p class="lead">ご見学・体験コース見学もお気軽にどうぞ！</p>
    <span class="mail">メールでのお問い合わせはこちら</span>
    <span class="foot-brand"><i></i>鳥羽キッチン</span>
  </div>
  <p class="copyright">Copyright © Toba Kitchen School. All Rights Reserved.</p>
</footer>
</body>
</html>
```